Birchwell Agency Condominium mail merge

We need a marketing proposal letter design to do a mail merge to potential e customers. We included our logo and an example of my miserable attempt to create a template. We are looking for a modern and attractive proposal template. Here is our website https://www.birchwellagency.example to be used for any additional information needed about us and our services.

Target Market(s)

New prospects

Industry/Entity Type

Insurance Agency

Requirements
Must have
• My project must have a modern professional look with merge fields similar to the file uploaded with this project.
Nice to have
• it would like have a condominium and a car icon graphic depicting there is additional discounts for both quotes bundled.
Should not have
• My project should not have any other logos or company name

```html
<!DOCTYPE html>
<html lang="en">
<head>
<meta charset="utf-8">
<title>Birchwell Agency – Condo Proposal Letter</title>
<link href="https://fonts.googleapis.com/css2?family=Mukta:wght@400;500;600&family=Montserrat:wght@600;700;800&family=Noto+Serif:wght@400;700&family=Great+Vibes&display=swap" rel="stylesheet">
<style>
  :root{
    --orange:#f47f20;
    --green:#3cb54a;
    --green-dark:#238a32;
    --blue:#27a7ee;
    --navy:#2b2d7a;
    --ink:#333;
    --muted:#666;
    --row-alt:#e8e8e8;
    --red:#d0112b;
    --lime:#f7ec13;
  }
  *{margin:0;padding:0;box-sizing:border-box}
  html,body{width:848px;height:1200px;overflow:hidden;background:#fff}
  .page{position:relative;width:848px;height:1200px;font-family:"Mukta",sans-serif;color:var(--ink)}
  .abs{position:absolute}

  .brand{left:34px;top:34px;display:flex;align-items:center;gap:10px}
  .brand-dot{width:34px;height:34px;border-radius:50%;background:var(--orange)}
  .brand-name{font-family:"Mukta",sans-serif;font-weight:600;font-size:30px;color:var(--green);line-height:1}

  .recipient{left:38px;top:124px;font-family:"Noto Serif",serif;font-size:11.5px;line-height:22.7px;color:#222}
  .recipient .lead{font-size:15px}

  .promo{left:595px;top:14px;width:241px;height:194px;border:2px solid var(--navy);border-radius:22px;overflow:hidden;background:var(--blue)}
  .promo-icon{left:7px;top:26px}
  .promo-head{left:40px;top:22px;font-family:"Montserrat",sans-serif;color:#fff;line-height:1}
  .promo-head .small{font-size:11px;font-weight:700}
  .promo-head .big{font-size:25px;font-weight:800;letter-spacing:.5px}
  .promo-scene{left:0;top:12px;right:0;height:138px}
  .promo-foot{left:0;right:0;top:142px;bottom:0;background:var(--green);border-top:3px solid #fff;color:#fff;font-family:"Montserrat",sans-serif;font-size:7px;line-height:8.8px;text-align:center;padding-top:6px;white-space:nowrap}
  .promo-foot b{font-weight:700}
  .promo-foot .hl{color:var(--lime);font-weight:700}

  .proposal{right:24px;top:229px;text-align:right}
  .proposal h1{font-family:"Montserrat",sans-serif;font-weight:700;font-size:17px;color:var(--green);line-height:1}
  .proposal .date{font-family:"Noto Serif",serif;font-size:11.5px;margin-top:8px;color:#333}

  .intro{left:38px;top:333px;width:780px;font-size:13.2px;line-height:21.5px;text-align:justify}
  .intro .greet{font-weight:600}

  .quote{left:34px;top:462px;width:779px}
  .addr-row{display:grid;grid-template-columns:231px 232px 106px 106px 104px;height:29px;border:1.5px solid var(--orange)}
  .addr-row div{font-weight:600;font-size:12px;padding:5px 0 0 19px;border-left:1.5px solid var(--orange);color:#222}
  .addr-row div:first-child{border-left:0}
  .cov-head{height:35px;background:var(--orange);color:#fff;font-size:14px;font-weight:500;display:flex;align-items:center;letter-spacing:.3px}
  .cov-head span:first-child{margin-left:28px;width:272px}
  .cov-body{position:relative;border:1px solid #ccc;border-top:0}
  .cov-row{display:flex;height:28.5px;align-items:center;font-size:12px;color:var(--muted);width:493px}
  .cov-row:nth-child(even){background:var(--row-alt)}
  .cov-row span:first-child{margin-left:23px;width:278px}
  .cov-row.strong span:first-child{color:#111;font-weight:600}
  .cov-row.strong span:last-child{font-weight:600}
  .premium{position:absolute;left:493px;top:1px;width:286px;bottom:2px;background:var(--green);color:#fff;font-family:"Noto Serif",serif;font-weight:700;text-align:center;display:flex;flex-direction:column;justify-content:center}
  .premium .label{font-size:13px}
  .premium .amount{font-size:20px;line-height:1.1}

  .disclaimer{left:47px;top:778px;width:760px;font-size:12px;line-height:21px;color:var(--red);font-weight:500}
  .closing{left:38px;top:832px;width:780px;font-size:13.2px;line-height:21.5px}
  .signoff{left:34px;top:916px;font-size:13.2px}
  .signature{left:34px;top:946px;font-family:"Great Vibes",cursive;font-size:30px;color:#1d1a4a}
  .sig-line{left:31px;top:988px;width:166px;height:1px;background:#999}
  .sig-title{left:34px;top:994px;font-family:"Montserrat",sans-serif;font-weight:600;font-size:12px;letter-spacing:1.6px;color:#222}

  .footer-shape{left:0;top:1070px}
  .footer-text{right:12px;top:1130px;text-align:right;font-family:"Noto Serif",serif;font-size:13px;line-height:21.5px;color:#fff;letter-spacing:.3px}
</style>
</head>
<body>
<div class="page">

  <div class="brand abs"><span class="brand-dot"></span><span class="brand-name">Birchwell Agency</span></div>

  <div class="recipient abs">
    <div class="lead">«encodedimbno»</div>
    <div>«first_name1» «last_name1»</div>
    <div>&lt;&lt;Address&gt;&gt;</div>
    <div>&lt;&lt;Address2&gt;&gt;</div>
    <div>&lt;&lt;City&gt;&gt;, &lt;&lt;State&gt;&gt;, &lt;&lt;Zip&gt;&gt;</div>
    <div class="lead">«presorttrayid»</div>
  </div>

  <div class="promo abs">
    <div class="promo-scene abs" role="img" aria-label="Red sports car parked in front of a two-storey house with a porch" style="background:linear-gradient(90deg,rgba(39,167,238,0) 40%,#b9a892 70%,#6f8a4a 100%),linear-gradient(0deg,#7a9a4e 0%,rgba(39,167,238,0) 35%)"></div>
    <svg class="promo-icon abs" width="28" height="28" viewBox="0 0 28 28" aria-hidden="true">
      <circle cx="14" cy="14" r="11.5" fill="none" stroke="#fff" stroke-width="2.5"/>
      <path d="M14 8v12M8 14h12" stroke="#fff" stroke-width="3"/>
    </svg>
    <div class="promo-head abs"><div class="small">COMBINE &amp;</div><div class="big">$AVE</div></div>
    <div class="promo-foot abs">
      Switch your <b>Condominium</b> and <b>Auto Insurance</b><br>
      policy by visiting <span class="hl">birchwellagency.example</span> today<br>
      or calling <span class="hl">407.555.0142</span> to take advantage of<br>
      additional discounts.
    </div>
  </div>

  <div class="proposal abs">
    <h1>PROPOSAL NO</h1>
    <div class="date">Date: &lt;&lt;DATE&gt;&gt;</div>
  </div>

  <div class="intro abs">
    <div class="greet">Respected Sir,</div>
    We have saved our clients $100s on their Condo Insurance. Call us at 407-555-0142 so we can do the same for you! Bundle your Condo and Auto insurance together for additional savings with a multi-policy discount. Below is a sample Condo Insurance policy purchased recently in Orlando from Birchwell Insurance Agency.
  </div>

  <div class="quote abs">
    <div class="addr-row">
      <div>&lt;&lt;Address&gt;&gt;</div><div>&lt;&lt;Address2&gt;&gt;</div><div>&lt;&lt;City&gt;&gt;</div><div>&lt;&lt;State&gt;&gt;</div><div>&lt;&lt;Zip&gt;&gt;</div>
    </div>
    <div class="cov-head"><span>COVERAGE</span><span>LIMIT</span></div>
    <div class="cov-body">
      <div class="cov-row"><span>Personal Property Protection</span><span>&lt;ColumnQ&gt;</span></div>
      <div class="cov-row"><span>Increased Additional Living Expense</span><span>20%</span></div>
      <div class="cov-row"><span>Loss Assessments</span><span>$2,000</span></div>
      <div class="cov-row"><span>Family Liability Protection</span><span>$100,000</span></div>
      <div class="cov-row"><span>Building Property Protection</span><span>&lt;ColumnK&gt;</span></div>
      <div class="cov-row"><span>Building Codes Coverages</span><span>25%</span></div>
      <div class="cov-row strong"><span>All Perils Deductible</span><span>$500</span></div>
      <div class="cov-row strong"><span>Hurricane&nbsp; Deductible</span><span>$500</span></div>
      <div class="premium"><div class="label">Total Annual Premium:</div><div class="amount">&lt;&lt;Yearly Premium&gt;&gt;</div></div>
    </div>
  </div>

  <p class="disclaimer abs">***The quoted premium is a sample premium based on a recent policy purchased in Orlando. Premium will differ based on information obtained on your application***</p>

  <p class="closing abs">If you are tired of paying too much for Condo Insurance and are wanting all of your insurance needs handled under one agency, then call us at 407-555.0142. One call is all it takes to see if you’ve got the right coverage at the right price.</p>

  <div class="signoff abs">Sincerely,</div>
  <div class="signature abs">Martin Hale</div>
  <div class="sig-line abs"></div>
  <div class="sig-title abs">[ AGENCY PRINCIPAL ]</div>

  <svg class="footer-shape abs" width="848" height="130" viewBox="0 1070 848 130" aria-hidden="true">
    <rect x="0" y="1122" width="848" height="78" fill="var(--orange)"/>
    <polygon points="0,1131 67,1081 297,1200 0,1200" fill="var(--green)"/>
    <polygon points="67,1081 201,1122 146,1122" fill="var(--green-dark)"/>
  </svg>
  <div class="footer-text abs">
    <div><b>A:</b> 2450 Lakeview Parkway Ste. 310 Winter Park, FL 32789</div>
    <div><b>Phone:</b> 407 555 0199 <b>Email:</b> info@BirchwellAgency.example, <b>Website:</b> BirchwellAgency.example</div>
  </div>

</div>
</body>
</html>
```